VALMIRA/ VALMIRA GREY Business Card

We have two brands that we would like to show one 1 business card (front and back). We would to incorporate two different logos on one card (VALMIRA and VALMIRA GREY). Card can be two sided. Simple, sleek and professional.

We are a senior living provider.

www.valmira-example.com
www.valmiragrey-example.com

Target Market(s)

Professionals

Industry/Entity Type

Business

Font styles to use
Serif

Colors

Designer to choose colors to be used in the design.

Requirements
Must have
• Space for EMAIL, PHONE, WEBSITE
Nice to have
• Raised lettering or gloss lettering

```html
<!DOCTYPE html>
<html lang="en">
<head>
<meta charset="utf-8">
<title>Valmira / Valmira Grey Business Card</title>
<link rel="stylesheet" href="https://fonts.googleapis.com/css2?family=Cinzel:wght@400;500;600&family=Cormorant+Garamond:ital,wght@0,400;0,500;1,400&display=swap">
<style>
  :root {
    --backdrop: #3b3b3d;
    --card: #161617;
    --card-edge: #262628;
    --gloss: #5a5a5d;
    --gold: #c9a04a;
    --white: #f2f0ec;
    --muted: #9a9896;
  }
  * { margin: 0; padding: 0; box-sizing: border-box; }
  html, body {
    width: 800px; height: 1200px; overflow: hidden;
    background: var(--backdrop);
  }
  .canvas {
    position: relative; width: 800px; height: 1200px;
    display: flex; flex-direction: column; align-items: center; justify-content: center;
    gap: 150px;
  }
  .card {
    position: relative; width: 620px; height: 354px;
    background: var(--card);
    border: 1px solid var(--card-edge);
    box-shadow: 0 14px 30px rgba(0,0,0,0.45);
  }

  /* Front */
  .card-front {
    display: flex; flex-direction: column; align-items: center; justify-content: center;
  }
  .front-brand {
    display: flex; align-items: center; gap: 18px;
  }
  .brand-square {
    width: 44px; height: 44px; background: var(--gloss);
  }
  .front-name {
    font-family: "Cinzel", serif; font-weight: 500;
    font-size: 60px; letter-spacing: 4px; line-height: 1;
    color: var(--gloss);
  }
  .front-web {
    margin-top: 34px;
    font-family: "Cormorant Garamond", serif; font-size: 14px;
    letter-spacing: 4px; color: var(--gold);
  }

  /* Back */
  .card-back {
    display: flex; align-items: center;
  }
  .back-brand {
    width: 50%; padding-left: 44px;
    display: flex; flex-direction: column; align-items: flex-start;
  }
  .back-brand-row { display: flex; align-items: center; gap: 12px; }
  .brand-square-small { width: 22px; height: 22px; background: var(--gold); }
  .back-name {
    font-family: "Cinzel", serif; font-weight: 500;
    font-size: 30px; letter-spacing: 1px; color: var(--white);
  }
  .back-tagline {
    margin-top: 6px; padding-left: 34px;
    font-family: "Cormorant Garamond", serif; font-size: 13px;
    color: var(--gold); letter-spacing: 0.5px;
  }
  .divider {
    position: absolute; left: 50%; top: 70px; bottom: 70px;
    width: 1px; background: var(--gold);
  }
  .person {
    width: 50%; padding-left: 36px;
  }
  .person-name {
    font-family: "Cinzel", serif; font-size: 24px; letter-spacing: 1.5px;
    color: var(--gold);
  }
  .person-title {
    font-family: "Cormorant Garamond", serif; font-style: italic;
    font-size: 14px; color: var(--muted); margin-bottom: 22px;
  }
  .contact-list { list-style: none; }
  .contact-item {
    display: flex; align-items: center; gap: 10px; margin-bottom: 8px;
    font-family: "Cormorant Garamond", serif; font-size: 14px; color: var(--white);
  }
  .contact-icon { width: 14px; height: 14px; flex: none; }
</style>
</head>
<body>
<main class="canvas">
  <section class="card card-front" aria-label="Card front">
    <div class="front-brand">
      <span class="brand-square"></span>
      <span class="front-name">VALMIRA</span>
    </div>
    <p class="front-web">www.valmira-example.com</p>
  </section>

  <section class="card card-back" aria-label="Card back">
    <div class="back-brand">
      <div class="back-brand-row">
        <span class="brand-square-small"></span>
        <span class="back-name">VALMIRA GREY</span>
      </div>
      <p class="back-tagline">Executive Senior Care Services</p>
    </div>
    <span class="divider"></span>
    <div class="person">
      <h1 class="person-name">CLARA HENSLEY</h1>
      <p class="person-title">Managing Director</p>
      <ul class="contact-list">
        <li class="contact-item">
          <svg class="contact-icon" viewBox="0 0 14 14"><circle cx="7" cy="7" r="7" fill="#c9a04a"/><path d="M4.6 3.8l1.2 1.4-.6.9c.5 1 1.3 1.8 2.3 2.3l.9-.6 1.4 1.2-.7 1.1C6.6 9.9 4.1 7.4 3.9 4.5z" fill="#161617"/></svg>
          555-014-2283
        </li>
        <li class="contact-item">
          <svg class="contact-icon" viewBox="0 0 14 14"><circle cx="7" cy="7" r="7" fill="#c9a04a"/><rect x="3.5" y="4.6" width="7" height="4.8" fill="none" stroke="#161617" stroke-width="0.9"/><path d="M3.5 4.6L7 7.4l3.5-2.8" fill="none" stroke="#161617" stroke-width="0.9"/></svg>
          info@valmiragrey-example.com
        </li>
        <li class="contact-item">
          <svg class="contact-icon" viewBox="0 0 14 14"><circle cx="7" cy="7" r="7" fill="#c9a04a"/><circle cx="7" cy="7" r="3.6" fill="none" stroke="#161617" stroke-width="0.8"/><ellipse cx="7" cy="7" rx="1.5" ry="3.6" fill="none" stroke="#161617" stroke-width="0.8"/><path d="M3.4 7h7.2" stroke="#161617" stroke-width="0.8"/></svg>
          www.valmiragrey-example.com
        </li>
      </ul>
    </div>
  </section>
</main>
</body>
</html>
```